Figlantern.com, vietnam local business need a webpage design

We need a web page design for a new business called Figlantern based in Ho Chi Min City, Vietnam. Figlantern sells high quality organic chestnut freshly roasted daily to provide a delicious healthy snack. Figlantern also has a sub-brand called ricepuddleway that sells soya bean curd. Figlantern domain name has been registered as figlantern.com and current Facebook page at Facebook.com/thefiglantern contains photos and other information.
We will like to see web page designs that is visually appealing and representative of our biz. The final design should communicates our core values and growth focus.
Updates

added ricepuddlway signage and Fb QR code

Target Market(s)

Consumer market, household, age range 18-50

Industry/Entity Type

Business

Requirements
Must have
• HTML5
Contain the following sections
- about us & contact us
- Outlets/Locations and locate-us (via google maps)
- Call to order
- Products
- Freshly Roasted Chestnuts
- Raw Chestnuts
- Soya Bean Curd
- Franchise Info
- Photo Gallery
Multi-language support - Vietnamese, English, Korean, Mandarin and Japanese
Mobile device support
- redirect based on browser header
- mobile device friendly format
- IPhone, iPad, Galaxy, Note
- locate/direct me to store (via google maps)
Should not have
• Flash, music, no pop-up

```html
<!DOCTYPE html>
<html lang="en">
<head>
<meta charset="utf-8">
<title>Figlantern</title>
<link rel="stylesheet" href="https://fonts.googleapis.com/css2?family=Satisfy&family=Source+Sans+3:ital,wght@0,400;0,600;1,400&display=swap">
<style>
:root{
  --rose:#b55a60;
  --rose-soft:#d6a2a6;
  --blush:#f2dfe1;
  --ink:#333333;
  --grey:#5a5a5a;
  --rule:#dcdcdc;
  --white:#ffffff;
}
*{margin:0;padding:0;box-sizing:border-box}
html,body{width:1200px;height:1079px;overflow:hidden;background:var(--white)}
body{position:relative;font-family:"Source Sans 3",sans-serif;color:var(--ink)}
.abs{position:absolute}

.logo{left:184px;top:26px;width:206px;height:206px;border-radius:50%;
  background:#b89a73;border:8px solid #efe5d3;box-shadow:0 0 0 2px #c9ad80;
  display:flex;align-items:center;justify-content:center;z-index:3}
.logo span{font-size:22px;font-weight:600;color:var(--white)}

.main-nav{left:450px;top:92px;display:flex;gap:0}
.main-nav a{font-family:"Satisfy",cursive;font-size:18px;color:var(--grey);text-decoration:none;margin-right:56px}
.main-nav a.current{color:var(--rose)}

.hero{left:420px;top:140px;width:601px;height:437px;
  background:linear-gradient(100deg,#ffffff 0%,#fdf8f8 35%,#f6e8e9 65%,var(--blush) 100%)}
.hero-art{left:193px;top:227px;width:304px;height:339px;border-radius:48% 48% 42% 42%;
  background:radial-gradient(circle at 50% 48%,#8a2e22 0%,#a0452f 28%,#c9a55a 55%,#ead9a8 75%,rgba(255,255,255,0) 100%)}
.hero-title{left:518px;top:248px;font-family:"Satisfy",cursive;font-size:68px;color:var(--rose);line-height:1}
.hero-text{left:524px;top:350px;width:480px;font-size:17px;letter-spacing:4.2px;line-height:26px;color:var(--grey)}
.slider-btn{top:537px;width:19px;height:19px;background:var(--rose-soft)}
.slider-btn svg{display:block}

.divider{left:181px;top:600px;width:840px;height:7px;border-top:4px solid #e6e6e6;border-bottom:1px solid var(--rule)}

.welcome-title{left:181px;top:630px;width:840px;text-align:center;font-size:23px;color:var(--rose)}
.welcome-text{left:181px;top:671px;width:840px;text-align:center;font-size:11.5px;line-height:20px}

.col-title{top:733px;font-size:19px;color:var(--rose)}
.photo{top:772px;width:252px;height:105px}
.photo.team{left:181px;background:linear-gradient(180deg,#3a3030 0%,#2a2424 55%,#5a2a2a 100%)}
.photo.items{left:464px;background:radial-gradient(circle at 40% 40%,#8e3b3a 0%,#6a2626 60%,#4a1a1a 100%)}
.photo.map{left:752px;width:269px;height:148px;background:linear-gradient(110deg,#e6e4cf 0%,#cfe0b0 45%,#a8c7e6 80%,#93bbe8 100%)}
.col-text{top:889px;width:260px;font-size:10.5px;line-height:17px}
.col-text.store{left:754px;top:932px;width:270px;font-style:italic}
.btn{top:952px;width:75px;height:21px;background:var(--rose);color:var(--white);font-size:8.5px;font-weight:600;
  display:flex;align-items:center;justify-content:center;text-decoration:none}

.footer{left:181px;top:1002px;width:840px;height:77px;background:var(--rose);color:var(--white)}
.footer-nav{left:30px;top:20px;display:flex;font-size:9px;font-weight:600}
.footer-nav a{color:var(--white);text-decoration:none}
.footer-nav i{font-style:normal;margin:0 26px}
.copyright{left:30px;top:44px;font-size:9px;font-weight:600}
.follow{left:677px;top:31px;font-size:9px;font-weight:600;display:flex;align-items:center;gap:5px}
.follow .dot{width:26px;height:26px;border-radius:50%;background:#3f86c4}
.follow .dot.mid{background:#2f7fa7}
.follow .dot.last{background:#55b2e6}
</style>
</head>
<body>
<div class="abs logo"><span>Figlantern</span></div>

<nav class="abs main-nav">
  <a class="current" href="#">Home</a>
  <a href="#">About us</a>
  <a href="#">Services</a>
  <a href="#">Products</a>
  <a href="#">Contact us</a>
</nav>

<section>
  <div class="abs hero"></div>
  <div class="abs hero-art" role="img" aria-label="Roasted chestnuts in an open spiky husk"></div>
  <h1 class="abs hero-title">Figlantern</h1>
  <p class="abs hero-text">Figlantern sells high quality organic chestnut freshly roasted daily to provide a delicious healthy snack</p>
  <a class="abs slider-btn" style="left:956px" href="#" aria-label="Previous"><svg width="19" height="19"><path d="M11 5 L7 9.5 L11 14" fill="none" stroke="#fff" stroke-width="1.2"/></svg></a>
  <a class="abs slider-btn" style="left:980px" href="#" aria-label="Next"><svg width="19" height="19"><path d="M8 5 L12 9.5 L8 14" fill="none" stroke="#fff" stroke-width="1.2"/></svg></a>
</section>

<div class="abs divider"></div>

<h2 class="abs welcome-title">Welcome to Figlantern</h2>
<p class="abs welcome-text">It is a long established fact that a reader will be distracted by the readable content of a page when looking at its layout. The point of using Lorem Ipsum is that it has a more-or-less normal distribution of letters, as opposed to using 'Content here, content here', making it look like readable English.</p>

<h3 class="abs col-title" style="left:179px">Our Team</h3>
<div class="abs photo team" role="img" aria-label="Team photo of staff standing beside the roasting cart"></div>
<p class="abs col-text" style="left:181px">Lorem ipsum' will uncover many web sites still in their infancy. Various versions have evolved over the years, sometimes by accident.</p>
<a class="abs btn" style="left:181px" href="#">READ MORE</a>

<h3 class="abs col-title" style="left:462px">Our Items</h3>
<div class="abs photo items" role="img" aria-label="Close-up of fresh chestnuts"></div>
<p class="abs col-text" style="left:464px">Lorem ipsum' will uncover many web sites still in their infancy. Various versions have evolved over the years, sometimes by accident.</p>
<a class="abs btn" style="left:464px" href="#">READ MORE</a>

<h3 class="abs col-title" style="left:752px">Store locator</h3>
<div class="abs photo map" role="img" aria-label="City map showing store locations"></div>
<p class="abs col-text store">Lorem ipsum' will uncover many web sites still in their infancy. Various versions have evolved...</p>

<footer class="abs footer">
  <nav class="abs footer-nav">
    <a href="#">HOME</a><i>|</i><a href="#">ABOUT US</a><i>|</i><a href="#">SERVICES</a><i>|</i><a href="#">PRODUCTS</a><i>|</i><a href="#">CONTACT US</a>
  </nav>
  <p class="abs copyright">© COPYRIGHT 2013. FIGLANTERN.  ALL RIGHTS RESERVED.</p>
  <div class="abs follow">FOLLOW US :
    <span class="dot" aria-label="Social link"></span>
    <span class="dot mid" aria-label="Social link"></span>
    <span class="dot last" aria-label="Social link"></span>
  </div>
</footer>
</body>
</html>
```